Brand Consulting Website, Simple Design/Layout that nails the "less is more" approach t...

I have an account on Quillbase through Tarnlink, so the design will need to be built there. I already have a logo, and the design of the website should at least compliment the look of the logo. The placeholder website where the logo can be seen is at www.valdromeconsulting.example. The purpose of the website at this point in time is not to drive business, but rather, to have a strong appearance and add some credibility to my already existing business.

The website should have some level of abstraction about it. I prefefer designs and shapes of images of people. The fewer people, the better. No stock photography of people standing around talking to each other.

Requirements
Must have
• The ability to work on my existing Quill Base Account
Should not have
• Stock photography of people standing around doing "business-y" stuff. That is sooo old and played out, and is the opposite of the type of message I am trying to portray.

```html
<!DOCTYPE html>
<html lang="en">
<head>
<meta charset="utf-8">
<title>Valdrome Consulting</title>
<link rel="stylesheet" href="https://fonts.googleapis.com/css2?family=Libre+Baskerville:ital,wght@0,400;0,700;1,400&family=Montserrat:wght@400;600;700&family=Open+Sans:ital,wght@0,400;0,600;1,400&display=swap">
<style>
:root{
  --orange:#f47a20;
  --black:#111111;
  --dark:#1d1d1d;
  --dark-2:#2a2a2a;
  --white:#ffffff;
  --grey:#666666;
  --line:#e6e6e6;
  --serif:'Libre Baskerville', Georgia, serif;
  --sans:'Montserrat', Arial, sans-serif;
  --body:'Open Sans', Arial, sans-serif;
}
*{box-sizing:border-box;margin:0;padding:0}
html,body{width:1200px;height:3571px;overflow:hidden;background:var(--white)}
body{position:relative;font-family:var(--body);color:var(--black)}

/* header */
.site-header{position:absolute;left:0;top:0;width:1200px;height:105px;background:var(--black)}
.brand{position:absolute;left:76px;top:18px;display:flex;align-items:center;gap:14px;color:var(--white);font-family:var(--sans);font-weight:700;font-size:24px;letter-spacing:1px}
.brand-mark{width:70px;height:70px;background:var(--white)}
.main-nav{position:absolute;right:80px;top:0;height:105px;display:flex;align-items:center;gap:34px;font-family:var(--sans);font-size:15px;color:var(--white);text-transform:uppercase}
.main-nav .active{color:var(--orange);position:relative}
.main-nav .active::after{content:"";position:absolute;left:-12px;right:-12px;bottom:-42px;height:6px;background:var(--orange)}
.main-nav .active::before{content:"";position:absolute;left:50%;bottom:-36px;margin-left:-8px;border:8px solid transparent;border-bottom-color:var(--orange)}
.search-icon{width:18px;height:18px}

/* hero */
.hero{position:absolute;left:0;top:105px;width:1200px;height:574px;background:linear-gradient(120deg,#3a2416 0%,#6b4226 40%,#8a5a36 70%,#4a2e1c 100%)}
.hero-card{position:absolute;left:538px;top:92px;width:468px;height:445px;background:var(--white);text-align:center;padding-top:54px}
.hero-card h1{font-family:var(--sans);font-weight:700;font-size:44px;line-height:1.2;letter-spacing:1px;color:var(--black)}
.hero-card p{font-size:16px;line-height:1.7;color:var(--grey);margin:24px 58px 0}
.btn{display:inline-block;background:var(--orange);color:var(--white);font-family:var(--serif);font-size:17px;letter-spacing:1px;text-transform:uppercase}
.hero-card .btn{margin-top:16px;padding:15px 30px}
.slider-tab{position:absolute;left:519px;top:538px;width:171px;height:36px;background:var(--black);clip-path:polygon(0 0,100% 0,90% 100%,0 100%);display:flex;align-items:center;justify-content:center;gap:9px;padding-right:16px}
.slider-tab i{width:11px;height:11px;border-radius:50%;background:var(--white)}
.slider-tab i.on{background:var(--orange)}

/* welcome */
.welcome{position:absolute;left:0;top:679px;width:1200px;height:483px;text-align:center}
.welcome h2{font-family:var(--serif);font-size:44px;line-height:1.25;margin-top:66px;font-weight:400}
.welcome h2 .accent{color:var(--orange);display:block}
.welcome p{font-size:13.5px;line-height:2.2;color:var(--grey);width:760px;margin:22px auto 0}
.welcome p + p{margin-top:8px}
.welcome .btn{margin-top:26px;padding:15px 28px}

/* services */
.service{position:absolute;width:595px;height:426px}
.service span{position:absolute;left:44px;bottom:30px;font-family:var(--serif);font-size:21px;color:var(--white)}
.s1{left:0;top:1162px;background:linear-gradient(135deg,#c8784a,#6a3a22 60%,#2a1a12)}
.s2{left:605px;top:1162px;background:linear-gradient(180deg,#e6e6e6,#8c8c8c 70%,#3a3a3a)}
.s3{left:0;top:1598px;background:linear-gradient(135deg,#4a3a30,#2b2522 60%,#1a1716)}
.s4{left:605px;top:1598px;background:linear-gradient(135deg,#6c7f8c,#3a4650 60%,#1c2228)}

/* clients */
.clients-title{position:absolute;left:0;top:2080px;width:1200px;text-align:center;font-family:var(--serif);font-size:42px}
.client-grid{position:absolute;left:195px;top:2174px;width:810px;height:255px;display:grid;grid-template-columns:repeat(4,1fr);grid-template-rows:repeat(2,1fr)}
.client{display:flex;align-items:center;justify-content:center;gap:10px;font-family:var(--serif);font-weight:700;font-size:20px;color:#2b3f6b;border-right:1px solid var(--line);border-bottom:1px solid var(--line)}
.client:nth-child(4n){border-right:0}
.client:nth-child(n+5){border-bottom:0}
.client .dot{width:16px;height:16px;background:var(--orange)}

/* brand test */
.brand-test{position:absolute;left:0;top:2505px;width:1200px;height:316px;background:var(--orange);color:var(--white)}
.brand-test h2{position:absolute;left:79px;top:84px;font-family:var(--serif);font-weight:700;font-size:40px}
.brand-test p{position:absolute;left:79px;top:144px;font-style:italic;font-size:17px}
.btn-outline{position:absolute;left:79px;top:185px;width:185px;height:50px;border:2px solid var(--white);font-family:var(--serif);font-size:16px;text-transform:uppercase;display:flex;align-items:center;justify-content:center}
.mascot{position:absolute;left:948px;top:2560px;width:244px;height:356px;border-radius:45% 45% 30% 30%;background:radial-gradient(ellipse at 55% 35%,#f6d9a8,#e49a4a 55%,#b8621f);z-index:2}

/* testimonial */
.testimonial{position:absolute;left:0;top:2821px;width:1200px;height:750px;background:var(--dark);overflow:hidden}
.ring{position:absolute;left:274px;top:-296px;width:642px;height:642px;border-radius:50%;border:2px solid var(--orange);background:var(--dark-2)}
.avatar{position:absolute;left:250px;top:65px;width:131px;height:131px;border-radius:50%;border:4px solid var(--orange);background:radial-gradient(circle at 50% 40%,#e8a06a,#b9662e)}
.quote{position:absolute;left:419px;top:86px;width:500px;font-style:italic;font-size:15px;line-height:1.95;color:#cfcfcf}
.client-name{position:absolute;left:638px;top:216px;font-size:14px;color:var(--orange);text-transform:uppercase}
.client-name::before{content:"";display:inline-block;width:14px;height:2px;background:var(--orange);vertical-align:middle;margin-right:8px}

/* contact */
.hello{position:absolute;left:0;top:3228px;width:1200px;text-align:center;font-family:var(--serif);font-weight:700;font-size:34px;color:var(--white)}
.call{position:absolute;left:80px;top:3340px;width:306px;text-align:center;color:#cfcfcf;font-size:15px}
.call strong{display:block;font-family:var(--serif);font-weight:400;font-size:30px;color:var(--white);margin-top:8px}
.get-in-touch{position:absolute;left:505px;top:3340px;width:188px;height:50px;display:flex;align-items:center;justify-content:center;padding:0}
.connect{position:absolute;left:860px;top:3340px;width:200px;text-align:center;color:#cfcfcf;font-size:15px}
.socials{display:flex;justify-content:center;gap:10px;margin-top:12px}
.socials i{width:40px;height:40px;border-radius:5px;background:var(--white)}
.footer-rule{position:absolute;left:80px;top:3457px;width:1040px;height:1px;background:#333}
.footer-links{position:absolute;left:0;top:3490px;width:1200px;text-align:center;color:#cfcfcf;font-size:13px;line-height:1.9}
</style>
</head>
<body>

<header class="site-header">
  <div class="brand"><div class="brand-mark"></div>Valdrome</div>
  <nav class="main-nav">
    <span class="active">Home</span><span>About</span><span>Services</span><span>Clients</span><span>Contact Us</span>
    <svg class="search-icon" viewBox="0 0 18 18"><circle cx="7.5" cy="7.5" r="5.5" fill="none" stroke="#fff" stroke-width="2.2"/><line x1="11.5" y1="11.5" x2="16.5" y2="16.5" stroke="#fff" stroke-width="2.6"/></svg>
  </nav>
</header>

<section class="hero" role="img" aria-label="Photo of a wooden desk with a cup of coffee, a phone, a pen and leaves">
  <div class="hero-card">
    <h1>A SPECIALIZED<br>BRAND<br>CONSULTING</h1>
    <p>We help our clients identify and develop protectable source identifiers through asset creation-oriented strategies.</p>
    <span class="btn">Contact Us</span>
  </div>
  <div class="slider-tab"><i></i><i></i><i class="on"></i><i></i><i></i></div>
</section>

<section class="welcome">
  <h2><span class="accent">Welcome To</span>Valdrome Consulting</h2>
  <p>Lorem Ipsum is simply dummy text of the printing and typesetting industry. Lorem Ipsum has been the industry's standard dummy text ever since the hen an unknown printer took a galley</p>
  <p>Lorem Ipsum is simply dummy text of the printing and typesetting industry. Lorem Ipsum has been the industry's standard dummy text ever since the 1500s, when an unknown printer took a galley of type and scrambled it to make a type specimen book. It has survived not only five centuries, but also the leap into electronic</p>
  <span class="btn">Learn More</span>
</section>

<div class="service s1" role="img" aria-label="Photo of a hand using a tablet showing a bar chart, warm orange tint"><span>Brand Research</span></div>
<div class="service s2" role="img" aria-label="Photo of a man drawing business sketches on a whiteboard"><span>Brand Strategy</span></div>
<div class="service s3" role="img" aria-label="Top view of a desk with a laptop, camera and plants"><span>Creative and Design</span></div>
<div class="service s4" role="img" aria-label="Photo of a team in a meeting room"><span>Management</span></div>

<h2 class="clients-title">Clients</h2>
<div class="client-grid">
  <div class="client"><i class="dot"></i>Harlow</div>
  <div class="client">Marque Studio</div>
  <div class="client">Orvel Brand</div>
  <div class="client">KTR Consulting</div>
  <div class="client">Pellin</div>
  <div class="client">Nemo Advisory</div>
  <div class="client">Drift</div>
  <div class="client">Ashwing</div>
</div>

<section class="brand-test">
  <h2>How Strong is Your Brand?</h2>
  <p>Take our brand strength test and get a customised report</p>
  <span class="btn-outline">Get Started</span>
</section>
<div class="mascot" role="img" aria-label="Illustration of a tiger lying over the edge of the orange band"></div>

<section class="testimonial">
  <div class="ring"></div>
  <div class="avatar" role="img" aria-label="Client portrait"></div>
  <p class="quote">Lorem Ipsum is simply dummy text of the printing and typesetting industry. Lorem Ipsum has been the industry's standard dummy text ever since the hen an unknown printer took a galley</p>
  <span class="client-name">Client Name</span>
</section>

<h2 class="hello">Ready to say Hello to Valdrome ?</h2>
<div class="call">Please Call Us On<strong>123 456 7890</strong></div>
<span class="btn get-in-touch">Get In Touch</span>
<div class="connect">Connect With Us
  <div class="socials" aria-label="Social links"><i></i><i></i><i></i><i></i></div>
</div>
<div class="footer-rule"></div>
<div class="footer-links">Home | About | Services | Clients | Contact<br>©Valdrome Consulting - 2019 All Rights Reserved</div>

</body>
</html>
```